Bref créative
Business Card design for Property Management Company
Harborlight Stewards
Professional
Corwin Talbot
P.O. Box K-4183
Nassau, Bahamas
corwin@harborlightstewardsgroup.com

```html
<!DOCTYPE html>
<html lang="en">
<head>
<meta charset="utf-8">
<title>Harborlight Stewards – Business Card</title>
<link rel="stylesheet" href="https://fonts.googleapis.com/css2?family=Cinzel:wght@400;600&display=swap">
<style>
  :root {
    --stage: #e7e4df;
    --card-white: #ffffff;
    --brand-navy: #1f2d3d;
    --brand-blue: #1a67a8;
    --brand-blue-light: #2f86c8;
    --band-dark: #2b2e33;
    --band-dark-2: #3a3e44;
    --text-light: #ffffff;
    --text-muted: #b9bec6;
  }
  html, body {
    margin: 0;
    width: 1200px;
    height: 902px;
    overflow: hidden;
    background: var(--stage);
  }
  .business-card {
    position: absolute;
    left: 100px;
    top: 165px;
    width: 1000px;
    height: 572px;
    box-shadow: 0 18px 40px rgba(0,0,0,0.25);
  }
  .business-card svg { display: block; }
  .brand-name, .holder-name, .contact-line, .web-line {
    font-family: "Cinzel", Georgia, serif;
  }
  .brand-name { fill: var(--brand-navy); font-weight: 600; }
  .holder-name { fill: var(--text-light); font-size: 36px; font-weight: 400; letter-spacing: 1px; }
  .contact-line { fill: var(--text-light); font-size: 24px; font-weight: 400; }
  .contact-icon { fill: var(--text-light); }
  .contact-glyph { fill: var(--brand-blue); }
  .web-line { fill: var(--text-muted); font-size: 15px; letter-spacing: 1px; }
</style>
</head>
<body>
<div class="business-card">
  <svg width="1000" height="572" viewBox="0 0 1000 572" xmlns="http://www.w3.org/2000/svg">
    <defs>
      <linearGradient id="blueBand" x1="0" y1="0" x2="1" y2="1">
        <stop offset="0" stop-color="var(--brand-blue)"/>
        <stop offset="0.5" stop-color="var(--brand-blue-light)"/>
        <stop offset="1" stop-color="var(--brand-blue)"/>
      </linearGradient>
      <linearGradient id="darkBand" x1="0" y1="0" x2="0" y2="1">
        <stop offset="0" stop-color="var(--band-dark-2)"/>
        <stop offset="1" stop-color="var(--band-dark)"/>
      </linearGradient>
    </defs>

    <rect class="card-face" width="1000" height="572" fill="var(--card-white)"/>

    <path class="blue-band" d="M0 300 L470 300 L520 232 L1000 232 L1000 572 L0 572 Z" fill="url(#blueBand)"/>

    <path class="notch" d="M750 232 L790 232 L770 252 Z" fill="var(--band-dark)"/>

    <path class="dark-band" d="M330 572 C520 500 760 470 1000 430 L1000 572 Z" fill="url(#darkBand)"/>

    <g class="brand-lockup">
      <circle cx="330" cy="112" r="52" fill="var(--brand-blue)"/>
      <text class="brand-name" x="405" y="110" font-size="52">HARBORLIGHT</text>
      <text class="brand-name" x="407" y="150" font-size="32" letter-spacing="6">STEWARDS</text>
    </g>

    <text class="holder-name" x="955" y="288" text-anchor="end">CORWIN TALBOT</text>

    <g class="contact-list">
      <circle class="contact-icon" cx="42" cy="343" r="10"/>
      <path class="contact-glyph" d="M42 336 L35 343 L37 343 L37 349 L47 349 L47 343 L49 343 Z"/>
      <text class="contact-line" x="62" y="352">P.O. Box K-4183</text>
      <text class="contact-line" x="62" y="384">Nassau, Bahamas</text>

      <circle class="contact-icon" cx="42" cy="407" r="10"/>
      <rect class="contact-glyph" x="38" y="401" width="8" height="12" rx="2"/>
      <text class="contact-line" x="62" y="416">(242) 555-0148</text>

      <circle class="contact-icon" cx="42" cy="439" r="10"/>
      <rect class="contact-glyph" x="36" y="435" width="12" height="8"/>
      <text class="contact-line" x="62" y="448" font-size="21">CORWIN@HARBORLIGHTSTEWARDSGROUP.COM</text>

      <circle class="contact-icon" cx="42" cy="471" r="10"/>
      <circle class="contact-glyph" cx="42" cy="471" r="5"/>
      <text class="contact-line" x="62" y="480" font-size="21">WWW.HARBORLIGHTSTEWARDSGROUP.COM</text>
    </g>

    <text class="web-line" x="955" y="478" text-anchor="end">www.harborlightstewardsgroup.com</text>
  </svg>
</div>
</body>
</html>
```